Exhibition Stand Design for innovative Social Business

We are an innovative social business empowering people to value nature through ZUN, a complementary digital currency. We have attached the TEK_ZUN branding document, and are needing a design for our exhibition stand (https://fairbuildlab.com/produit/stand-parapluie-classic-pvc-3x4c/. The attached doc mocks up a stand on page 32, though we would like some messaging included, in line with our website www.tekzun.ch. You will see there how the branding concept has been implemented with the TEK:GROW, SHARE, THRIVE wording, as well as Everyone wins. Our green colours are included in the branding document. Many thanks!

Industry/Entity Type

Environment

Font styles to use
Other font styles liked:
• As per our attached fonts

Requirements
Must have
• Our attached branding guidelines gives our look and feel - Innovative / Dynamic / Vibrant / Reliable / Accessible / Connected.

```html
<!DOCTYPE html>
<html lang="en">
<head>
<meta charset="utf-8">
<title>TEK:ZUN exhibition stand</title>
<link rel="stylesheet" href="https://fonts.googleapis.com/css2?family=Montserrat:wght@600;700&family=Comfortaa:wght@700&display=swap">
<style>
  :root {
    --page: #eceded;
    --ink: #0a0a0a;
    --white: #ffffff;
    --green-left: #47e9a2;
    --green-mid: #3ded83;
    --green-right: #22f041;
    --ring-light: #c9f7db;
    --ring-glow: #8af3b4;
    --soft-bubble: rgba(255, 255, 255, 0.28);
  }
  * { margin: 0; padding: 0; box-sizing: border-box; }
  html, body {
    width: 1200px;
    height: 1000px;
    overflow: hidden;
    background: var(--page);
  }
  .stand {
    position: absolute;
    left: 100px;
    top: 110px;
    width: 1000px;
    height: 740px;
    overflow: hidden;
    background: linear-gradient(90deg, var(--green-left) 0%, var(--green-mid) 50%, var(--green-right) 100%);
    font-family: "Montserrat", sans-serif;
  }
  .bubble {
    position: absolute;
    border-radius: 50%;
    background: var(--soft-bubble);
  }
  .bubble--top-right { width: 560px; height: 560px; left: 700px; top: -60px; }
  .bubble--bottom-left { width: 380px; height: 380px; left: -90px; top: 520px; }
  .header-band {
    position: absolute;
    left: 0; top: 0;
    width: 100%;
    height: 150px;
    background: var(--white);
    border-bottom: 3px solid var(--ink);
  }
  .brand-name {
    position: absolute;
    left: 58px;
    top: 18px;
    font-weight: 700;
    font-size: 92px;
    letter-spacing: 2px;
    color: var(--ink);
  }
  .tagline {
    position: absolute;
    right: 48px;
    top: 60px;
    font-family: "Comfortaa", sans-serif;
    font-weight: 700;
    font-size: 48px;
    color: var(--ink);
  }
  .pillars {
    position: absolute;
    left: 0; top: 198px;
    width: 100%;
  }
  .pillar {
    position: absolute;
    top: 0;
    width: 240px;
  }
  .pillar--grow { left: 88px; }
  .pillar--share { left: 386px; }
  .pillar--thrive { left: 683px; }
  .pillar-badge { display: block; width: 240px; height: 240px; }
  .pillar-label {
    margin: 12px 0 0 62px;
    color: var(--white);
    line-height: 1;
  }
  .pillar-label .prefix {
    display: block;
    font-weight: 700;
    font-size: 22px;
    color: var(--ink);
  }
  .pillar-label .word {
    display: block;
    font-weight: 600;
    font-size: 46px;
    margin-top: 4px;
  }
</style>
</head>
<body>
  <main class="stand">
    <div class="bubble bubble--top-right"></div>
    <div class="bubble bubble--bottom-left"></div>

    <header class="header-band">
      <div class="brand-name">TEK:ZUN</div>
      <div class="tagline">everyone wins</div>
    </header>

    <section class="pillars">
      <div class="pillar pillar--grow">
        <svg class="pillar-badge" viewBox="0 0 240 240">
          <defs>
            <linearGradient id="ringFill" x1="0" y1="1" x2="1" y2="0">
              <stop offset="0" stop-color="#ffffff"/>
              <stop offset="1" stop-color="#8af3b4"/>
            </linearGradient>
          </defs>
          <circle cx="120" cy="120" r="114" fill="none" stroke="#0a0a0a" stroke-width="5"/>
          <circle cx="120" cy="120" r="103" fill="url(#ringFill)"/>
          <path d="M120 190 L50 118 C30 96 38 58 72 54 C94 52 110 64 120 80 C130 64 146 52 168 54 C202 58 210 96 190 118 Z" fill="#0a0a0a"/>
          <polyline points="76,126 108,126 118,104 130,146 140,118 150,126 194,126" fill="none" stroke="#c9f7db" stroke-width="7" stroke-linejoin="round" stroke-linecap="round"/>
        </svg>
        <div class="pillar-label"><span class="prefix">TEK:</span><span class="word">GROW</span></div>
      </div>

      <div class="pillar pillar--share">
        <svg class="pillar-badge" viewBox="0 0 240 240">
          <circle cx="120" cy="120" r="114" fill="none" stroke="#0a0a0a" stroke-width="5"/>
          <circle cx="120" cy="120" r="103" fill="url(#ringFill)"/>
          <circle cx="120" cy="120" r="84" fill="#0a0a0a"/>
          <text x="120" y="156" text-anchor="middle" font-family="Montserrat, sans-serif" font-weight="700" font-size="112" fill="#c9f7db">$</text>
        </svg>
        <div class="pillar-label"><span class="prefix">TEK:</span><span class="word">SHARE</span></div>
      </div>

      <div class="pillar pillar--thrive">
        <svg class="pillar-badge" viewBox="0 0 240 240">
          <circle cx="120" cy="120" r="114" fill="none" stroke="#0a0a0a" stroke-width="5"/>
          <circle cx="120" cy="120" r="103" fill="url(#ringFill)"/>
          <circle cx="120" cy="120" r="84" fill="#a8f0c4" stroke="#0a0a0a" stroke-width="4" role="img" aria-label="Globe illustration showing the continents"/>
        </svg>
        <div class="pillar-label"><span class="prefix">TEK:</span><span class="word">THRIVE</span></div>
      </div>
    </section>
  </main>
</body>
</html>
```